Sign Design for Truck Repair Shop center

Need a road-side sign for a pickup truck repair shop called HaulPoint Garage. The logo is attached and should be used on the sign. The background should be white and the main part of the logo should take up a large part of the sign so it can be easily read by passing traffic. The sign is 4 feet tall by 8 feet wide. Also need to add the website address" "www.HaulPointGarage-example.com" and "Call/Text 555.382.4607"

```html
<!DOCTYPE html>
<html lang="en">
<head>
<meta charset="utf-8">
<title>HaulPoint Garage – Roadside Sign</title>
<link href="https://fonts.googleapis.com/css2?family=Poppins:wght@500;600;700;800&display=swap" rel="stylesheet">
<style>
  :root {
    --page-bg: #b7b7b7;
    --sign-white: #ffffff;
    --plate-dark: #141414;
    --plate-mid: #2a2a2a;
    --brand-blue: #0b4fa0;
    --accent-blue: #2d7bd3;
    --text-white: #ffffff;
  }
  * { box-sizing: border-box; margin: 0; padding: 0; }
  html, body {
    width: 928px; height: 1200px; overflow: hidden;
    background: var(--page-bg);
    font-family: "Poppins", sans-serif;
  }
  .sign {
    position: absolute;
    left: 34px; top: 385px;
    width: 860px; height: 430px;
    background: var(--sign-white);
    box-shadow: 10px 14px 22px rgba(0,0,0,0.35);
    overflow: hidden;
  }
  .sign-plate {
    position: absolute;
    left: 0; right: 0; top: 196px; bottom: 0;
    background: linear-gradient(135deg, var(--plate-mid), var(--plate-dark) 55%, var(--plate-mid));
  }
  .brand {
    position: absolute;
    left: 0; right: 0; top: 48px;
    text-align: center;
  }
  .brand-name {
    font-weight: 800;
    font-size: 74px;
    line-height: 1;
    color: var(--brand-blue);
    letter-spacing: -1px;
  }
  .brand-tagline {
    margin-top: 14px;
    font-weight: 700;
    font-size: 21px;
    letter-spacing: 1.5px;
    color: var(--brand-blue);
  }
  .contact-line {
    position: absolute;
    left: 0; right: 0; top: 246px;
    display: flex; align-items: center; justify-content: center;
    gap: 18px;
    color: var(--text-white);
  }
  .contact-label { font-weight: 500; font-size: 46px; line-height: 1; }
  .contact-number { font-weight: 600; font-size: 50px; line-height: 1; }
  .phone-icon { width: 46px; height: 46px; flex: none; }
  .web-bar {
    position: absolute;
    left: 58px; right: 58px; top: 330px;
    height: 60px;
    background: var(--accent-blue);
    border-radius: 8px;
    display: flex; align-items: center; justify-content: center;
    color: var(--text-white);
    font-weight: 700;
    font-size: 37px;
    letter-spacing: -0.3px;
  }
</style>
</head>
<body>
  <div class="sign">
    <div class="sign-plate" role="img" aria-label="Black diamond-plate metal texture"></div>
    <div class="brand">
      <div class="brand-name">HaulPoint Garage</div>
      <div class="brand-tagline">YOUR TRUSTED PICKUP SPECIALISTS</div>
    </div>
    <div class="contact-line">
      <span class="contact-label">CALL/TEXT</span>
      <svg class="phone-icon" viewBox="0 0 46 46" aria-hidden="true">
        <circle cx="23" cy="23" r="23" fill="#2d7bd3"/>
        <path d="M15.5 12.5c1-.8 2.3-.6 3 .4l2.4 3.4c.6.9.5 2.1-.3 2.8l-1.6 1.4c1.2 2.7 3.2 4.8 5.9 6.1l1.5-1.6c.7-.8 1.9-.9 2.8-.3l3.4 2.3c1 .7 1.2 2.1.4 3l-1.7 2c-1 1.1-2.6 1.5-4 1-7.4-2.6-12.4-7.7-14.8-14.9-.5-1.4-.1-3 1-3.9z" fill="#ffffff"/>
        <path d="M26 13.5a7 7 0 0 1 6.5 6.5M26 9.5a11 11 0 0 1 10.5 10.5" stroke="#ffffff" stroke-width="2" fill="none" stroke-linecap="round"/>
      </svg>
      <span class="contact-number">555.382.4607</span>
    </div>
    <div class="web-bar">www.HaulPointGarage-example.com</div>
  </div>
</body>
</html>
```